Corvale Brochure - A new residential property investment development in Brisbane Queensland *

I need a brochure to entice and inspire customers of financial planners and alike to buy our investment property development, Corvale in Greenbank, Australia.

The brochure will be approximately 16 - 18 pages long and will follow a similar format (including maps etc) to the once attached in the uploaded files, however it is important that it has it's own unique style and brand identify. You will have access to all the renders, maps and autocad drawings that will need to be included in the brochure and will be linked in my dropbox link below.

The brochure should feel sophisticated and use the logo we've previously had developed on pixel forum. The background and text should also match the style guidelines of our logo's although happy for you to to get creative with the background as long as it is relevant and fits with the colours. For example stock photo's of tree's, people playing, sunlight etc are great - although the context should be in Australia.

There will be a bit of back and forth once I select the winning designer to ensure the brochure is perfect. I'll also need individual files of the masterplan.

Look forward to seeing your designs.

https://www.filemarrow.net/sh/qtmzx8v2pk4hd0r/BBKw7tnP3_QZmvUe9Lh4rxsk?dl=0

Target Market(s)

Financial Planners and their consumer customers

Industry/Entity Type

Real Estate Development

Font styles to use
Other font styles liked:
• Monserrat - as per branding guidelines

Requirements
Must have
• At least all the elements that exist in the example brochures and outlined in the content

dropbox link - https://www.filemarrow.net/sh/qtmzx8v2pk4hd0r/BBKw7tnP3_QZmvUe9Lh4rxsk?dl=0

```html
<!DOCTYPE html>
<html lang="en">
<head>
<meta charset="utf-8">
<title>Corvale Brochure – Opening Spread</title>
<link rel="stylesheet" href="https://fonts.googleapis.com/css2?family=Montserrat:wght@500;600;800&display=swap">
<style>
  :root {
    --backdrop: #bcd3e6;
    --cover-blue: #1c5474;
    --cover-blue-deep: #174763;
    --photo-dark: #1d2a36;
    --photo-denim: #3c5f86;
    --photo-green: #5d6e4a;
    --photo-light: #e7ecea;
    --heading-blue: #4a86ad;
    --menu-text: #d8e6ef;
    --page-shadow: rgba(40, 70, 100, 0.28);
  }
  * { box-sizing: border-box; margin: 0; padding: 0; }
  html, body {
    width: 1200px;
    height: 900px;
    overflow: hidden;
    background: var(--backdrop);
    font-family: "Montserrat", sans-serif;
  }
  .spread {
    position: absolute;
    left: 90px;
    top: 255px;
    width: 1020px;
    height: 390px;
    display: flex;
    box-shadow: 0 14px 30px var(--page-shadow);
  }
  .page {
    position: relative;
    width: 50%;
    height: 100%;
    overflow: hidden;
  }
  .page--contents {
    background: var(--cover-blue);
  }
  .contents-list {
    position: absolute;
    left: 44px;
    bottom: 92px;
    list-style: none;
  }
  .contents-list li {
    font-size: 7px;
    font-weight: 600;
    letter-spacing: 0.14em;
    text-transform: uppercase;
    color: var(--menu-text);
    line-height: 12px;
  }
  .page-photo {
    position: absolute;
    top: 0;
    bottom: 0;
  }
  .page-photo--left {
    right: 0;
    width: 150px;
    background: linear-gradient(90deg, var(--cover-blue) 0%, var(--photo-dark) 45%, #2a3642 100%);
  }
  .page-photo--right {
    left: 0;
    width: 100%;
    background:
      radial-gradient(ellipse 120px 90px at 22% 48%, var(--photo-denim) 0%, transparent 100%),
      radial-gradient(ellipse 220px 160px at 62% 38%, var(--photo-green) 0%, transparent 100%),
      radial-gradient(ellipse 180px 140px at 86% 22%, var(--photo-light) 0%, transparent 100%),
      linear-gradient(180deg, #6d7a66 0%, #4a5550 55%, #dfe3e4 78%, #f1f2f3 100%);
  }
  .gutter {
    position: absolute;
    left: 50%;
    top: 0;
    width: 24px;
    height: 100%;
    margin-left: -12px;
    background: linear-gradient(90deg, transparent, rgba(0,0,0,0.22), transparent);
    pointer-events: none;
  }
  .spread-heading {
    position: absolute;
    right: 40px;
    top: 74px;
    text-align: right;
    font-size: 27px;
    font-weight: 800;
    line-height: 1.0;
    color: var(--heading-blue);
  }
</style>
</head>
<body>
  <section class="spread">
    <div class="page page--contents">
      <ul class="contents-list">
        <li>Vision</li>
        <li>Location &amp; Amenity</li>
        <li>Sense of Community</li>
        <li>Investment</li>
        <li>Points of Interest</li>
        <li>Masterplan</li>
        <li>House Plans</li>
        <li>Package Inclusions</li>
      </ul>
      <div class="page-photo page-photo--left" role="img" aria-label="Left edge of a café photo: person in a denim shirt, softly out of focus"></div>
    </div>
    <div class="page page--feature">
      <div class="page-photo page-photo--right" role="img" aria-label="Photograph of a person in a denim shirt resting a hand beside a white coffee cup at a sunlit outdoor café table"></div>
      <h1 class="spread-heading">Creating<br>a sense<br>of place</h1>
    </div>
    <div class="gutter"></div>
  </section>
</body>
</html>
```